Halvern Construction - Brochure

We need a graphic design for a company based in Vancouver, BC, Canada called 'Halvern Construction Ltd'. Halvern Construction is a company that specializes in building custom residential houses. The company has been in business for approximately 20 years. We specialize in building 1, 2, and 3 story houses as well as Laneway (coach) homes. We allow our customers to build there dream homes by working with our architects to build a design of there choosing. They also have all the options of choosing whatever materials they want in there houses for eg. doors, faucets, bathroom fixtures etc.We would like to see designs that use the color red and white.
Our second division of Halvern Construction is called "Halvern Environmental" which specializes in the testing and removal of hazardous materials i.e asbestos. The testing and removal of asbestos is a municipal requirement throughout the lower mainland. All hazardous materials must be removed prior to the demolition of any residential building. It would be nice to have parts of the brochure use the colour green to emphazise this companies colour.
Aside from other things, the brochure must mention:
- "Direct to builder, no real estate agent, No 3rd party commission"
- "We also specialize in Laneway Homes"
- "Customize your house the way you want! Come on in for a free consultation"
Also, the contact information:
- Office Address: 2837 Marlowe Street, Vancouver, BC V6R 1K9
- Email: info@halvernbuilds.example
- Phone: 604-555-0176
- Fax: 604-555-0177
- Website: www.halvernbuilds.example
We've re-read our task description and it says "We need a graphic design...". Actually what we meant to say is we are looking for someone who can create us a BROCHURE/FLYER, which can include graphic designs as we do not have one at the moment. We're looking for someone who can create a brochure that encompasses the information already provided and more. More information can be provided and probably will be provided once some designs have come our way. Sorry for the confusion!
We also want to include the following on the brochure:
We can BUY your old house for the purposes of resale or build a new house
We can TRADE your old house for one of our newly built houses
Target Market(s)
ages between 30-60 years old. People who can afford to build a home,

```html
<!DOCTYPE html>
<html lang="en">
<head>
<meta charset="utf-8">
<title>Halvern Construction – Brochure</title>
<link rel="stylesheet" href="https://fonts.googleapis.com/css2?family=Open+Sans:wght@400;600;700&display=swap">
<style>
:root{
  --stage:#2a2a2a;
  --navy:#0b3565;
  --navy-deep:#062a52;
  --sky-top:#3f6fc4;
  --sky-mid:#7fb4e6;
  --sky-low:#4b7cc8;
  --white:#ffffff;
  --ink:#0b2f63;
  --red:#c8202f;
  --red-soft:#fbe9ea;
  --green:#2e8b3e;
  --green-soft:#e8f4ea;
  --accent:#f5a300;
  --fold:rgba(255,255,255,0.35);
  --fold-inside:#ececec;
}
*{margin:0;padding:0;box-sizing:border-box}
html,body{width:1200px;height:1000px;overflow:hidden}
body{background:var(--stage);font-family:"Open Sans",Arial,sans-serif;position:relative}
.sheet{position:absolute;left:276px;width:619px;overflow:hidden}
.sheet-outer{top:13px;height:478px}
.sheet-inner{top:509px;height:478px;background:var(--white)}

/* outer spread */
.panel-back{position:absolute;left:0;top:0;width:310px;height:349px;
  background:linear-gradient(180deg,var(--sky-top) 0%,var(--sky-mid) 45%,var(--sky-low) 100%)}
.placeholder-label{position:absolute;left:0;width:310px;top:144px;text-align:center;
  font-weight:700;font-size:21px;color:#0a0a0a}
.cover-photo{position:absolute;left:310px;top:0;width:309px;height:349px;
  background:linear-gradient(180deg,#2f6fd0 0%,#5d96de 40%,#3b4a5c 62%,#1f8fd6 80%,#0f5fa8 100%)}
.contact-band{position:absolute;left:0;top:349px;width:619px;height:129px;background:var(--navy);
  border-top:2px solid var(--red)}
.fold-outer{position:absolute;left:310px;top:0;width:1px;height:478px;background:var(--fold)}
.back-contact{position:absolute;left:0;top:376px;width:300px;text-align:center;color:var(--white)}
.back-contact .company{font-weight:700;font-size:11px;line-height:14px}
.back-contact p{font-size:6.6px;font-weight:600;line-height:9px}
.back-contact .gap{margin-top:10px}
.back-contact .web{color:var(--accent)}
.back-contact .web span{color:var(--white)}
.front-title{position:absolute;right:22px;top:375px;text-align:right;color:var(--white)}
.front-title h1{font-weight:600;font-size:20px;line-height:24px}
.front-title .tagline{font-size:7.4px;letter-spacing:1.55px;line-height:9px}

/* inside spread */
.tab{position:absolute;top:29px;width:37px;height:420px;
  background:linear-gradient(180deg,var(--navy-deep) 0%,#1a74bd 50%,var(--navy-deep) 100%)}
.tab-left{left:0;border-radius:0 34px 34px 0}
.tab-right{right:0;border-radius:34px 0 0 34px}
.fold-inner{position:absolute;left:310px;top:0;width:1px;height:478px;background:var(--fold-inside)}
.about{position:absolute;left:43px;top:46px;width:118px;color:var(--ink)}
.about h2{font-size:7.6px;font-weight:700;padding-bottom:2px;border-bottom:1.5px solid var(--red);width:113px}
.about h3{font-size:7.2px;font-weight:700;margin-top:5px}
.about p{font-size:5.2px;font-weight:600;line-height:8.7px}
.about p + p{margin-top:8.7px}
.house-photo{position:absolute;left:175px;width:113px;box-shadow:0 0 2px rgba(0,0,0,0.3)}
.house-1{top:64px;height:81px;background:linear-gradient(180deg,#3d7fd6 0%,#a9c6e6 40%,#b9a48a 62%,#4f8f2e 80%,#3a7a22 100%)}
.house-2{top:154px;height:76px;background:linear-gradient(180deg,#cfdff0 0%,#e3cfa6 45%,#c9a77a 70%,#bfc6b0 100%)}
.house-3{top:239px;height:75px;background:linear-gradient(180deg,#3d86d8 0%,#8fbde8 35%,#d9d6c8 60%,#6a9a3a 82%,#4a7f2a 100%)}

/* inside right panel */
.offer{position:absolute;left:330px;top:46px;width:232px;color:var(--ink)}
.offer h2{font-size:7.6px;font-weight:700;padding-bottom:2px;border-bottom:1.5px solid var(--red)}
.benefits{list-style:none;margin-top:8px}
.benefits li{display:flex;align-items:flex-start;gap:5px;font-size:6.4px;font-weight:600;line-height:9px;margin-bottom:6px}
.benefits svg{flex:0 0 9px;width:9px;height:9px}
.deal-row{display:flex;gap:6px;margin-top:6px}
.deal{flex:1;background:var(--red-soft);border-left:3px solid var(--red);padding:6px 6px 7px}
.deal h4{font-size:8px;font-weight:700;color:var(--red);line-height:11px}
.deal p{font-size:5.6px;font-weight:600;line-height:8px}
.enviro{margin-top:12px;background:var(--green-soft);border-left:3px solid var(--green);padding:7px 8px 8px}
.enviro h3{font-size:7.6px;font-weight:700;color:var(--green);line-height:11px}
.enviro p{font-size:5.6px;font-weight:600;line-height:8.4px;color:#1f4d29}
.consult{margin-top:12px;background:var(--red);color:var(--white);padding:9px 10px;text-align:center}
.consult strong{display:block;font-size:8.4px;font-weight:700;line-height:12px}
.consult span{font-size:6.4px;font-weight:600;line-height:9px}
.offer-contact{margin-top:10px;font-size:6px;font-weight:600;line-height:9px;text-align:center}
</style>
</head>
<body>

<section class="sheet sheet-outer">
  <div class="panel-back"><div class="placeholder-label">Images/text</div></div>
  <div class="cover-photo" role="img" aria-label="Photo of a modern two-storey house with glass facade and a lit swimming pool at dusk"></div>
  <div class="contact-band"></div>
  <div class="fold-outer"></div>

  <div class="back-contact">
    <div class="company">Halvern Construction Ltd</div>
    <p>2837 Marlowe Street, Vancouver, BC V6R 1K9</p>
    <p class="gap">Phone: 604-555-0176</p>
    <p>Fax: 604-555-0177</p>
    <p class="gap web">Email: info@halvernbuilds.example</p>
    <p class="web">Website: <span>www.halvernbuilds.example</span></p>
  </div>

  <div class="front-title">
    <h1>Halvern Construction Ltd</h1>
    <div class="tagline">BUILD YOUR RESIDENTIAL HOUSE</div>
  </div>
</section>

<section class="sheet sheet-inner">
  <div class="tab tab-left"></div>
  <div class="tab tab-right"></div>
  <div class="fold-inner"></div>

  <div class="about">
    <h2>Halvern Construction Ltd</h2>
    <h3>About us</h3>
    <p>Halvern Construction is a company that specializes in building custom residential houses. The company has been in business for approximately 20 years. We specialize in building 1, 2, and 3 story houses as well as Laneway (coach) homes. We allow our customers to build their dream homes by working with our architects to build a design of their choosing. They also have all the options of choosing whatever materials they want in their houses, e.g. doors, faucets, bathroom fixtures etc.</p>
    <p>Our second division of Halvern Construction is called "Halvern Environmental" which specializes in the testing and removal of hazardous materials i.e. asbestos. The testing and removal of asbestos is a municipal requirement throughout the lower mainland. All hazardous materials must be removed prior to the demolition of any residential building.</p>
  </div>

  <div class="house-photo house-1" role="img" aria-label="Photo of a two-storey suburban house with a green lawn"></div>
  <div class="house-photo house-2" role="img" aria-label="Photo of a beige stucco house with arched windows"></div>
  <div class="house-photo house-3" role="img" aria-label="Photo of a family house with a garage under blue sky"></div>

  <div class="offer">
    <h2>Why build with us</h2>
    <ul class="benefits">
      <li><svg viewBox="0 0 10 10"><circle cx="5" cy="5" r="5" fill="#c8202f"/><path d="M2.6 5.2 4.3 6.8 7.4 3.4" fill="none" stroke="#fff" stroke-width="1.3"/></svg>Direct to builder, no real estate agent, No 3rd party commission</li>
      <li><svg viewBox="0 0 10 10"><circle cx="5" cy="5" r="5" fill="#c8202f"/><path d="M2.6 5.2 4.3 6.8 7.4 3.4" fill="none" stroke="#fff" stroke-width="1.3"/></svg>We also specialize in Laneway Homes</li>
      <li><svg viewBox="0 0 10 10"><circle cx="5" cy="5" r="5" fill="#c8202f"/><path d="M2.6 5.2 4.3 6.8 7.4 3.4" fill="none" stroke="#fff" stroke-width="1.3"/></svg>Custom 1, 2 and 3 story homes with the materials you choose</li>
    </ul>
    <div class="deal-row">
      <div class="deal">
        <h4>BUY</h4>
        <p>We can BUY your old house for the purposes of resale or build a new house</p>
      </div>
      <div class="deal">
        <h4>TRADE</h4>
        <p>We can TRADE your old house for one of our newly built houses</p>
      </div>
    </div>
    <div class="enviro">
      <h3>Halvern Environmental</h3>
      <p>Testing and removal of hazardous materials such as asbestos, required by municipalities throughout the lower mainland before the demolition of any residential building.</p>
    </div>
    <div class="consult">
      <strong>Customize your house the way you want!</strong>
      <span>Come on in for a free consultation</span>
    </div>
    <div class="offer-contact">Phone: 604-555-0176 &nbsp;|&nbsp; www.halvernbuilds.example</div>
  </div>
</section>

</body>
</html>
```